poster design for mountainbike & trail run race

I am looking for a poster design for a charitable mountain bike and trail run race. It should be something fun, colorful, epic, which can attract participants. The area in which the competition takes place is dominated by hills and by the Nera river which has a beautiful gorge. I am attaching our last year poster, which we like, but would like this year to be a bit more epic, exciting for the possible participants. The poster should have a place where I can add the sponsor logos (approx 20 logos), which I will do by myself, in the following months (will need editable design format). We will also need the poster in both 16x9 and 4x3 formats.
Text:
Headline: "Dealul Vultan Mountain Bike and Trail Run Race"
small headline: "Editia a-7a"
small headline: "Valea Brantului, 8-9 IUNIE 2024"
other text:
"8 IUNIE - Concurs Mountain Bike & Concert
9 IUNIE - Concurs Trail Run"
text for enrollments: "inscrieri pe www.brantovelo.ro"

Thank you!

people aged 18-50, doing sports, participating to competitions

• clean, proefesional design. The poster will be presented in social media as well on bilboards

```html
<!DOCTYPE html>
<html lang="ro">
<head>
<meta charset="utf-8">
<title>Dealul Vultan – Mountain Bike &amp; Trail Run Race</title>
<link href="https://fonts.googleapis.com/css2?family=Barlow+Condensed:ital,wght@0,700;0,800;1,700;1,800&family=Barlow:ital,wght@1,800&display=swap" rel="stylesheet">
<style>
  :root{
    --ink:#1f2a3a;
    --red:#d2381f;
    --orange:#ef7a2a;
    --amber:#f4a640;
    --paper:#ffffff;
    --brush:#2a1f1c;
  }
  html,body{margin:0;padding:0;overflow:hidden;background:var(--paper);}
  .poster{
    position:relative;width:1200px;height:675px;overflow:hidden;
    background:var(--paper);
    font-family:"Barlow Condensed","Arial Narrow",sans-serif;
    color:var(--ink);
  }
  .poster p,.poster h1{white-space:nowrap;}
  .scenery{position:absolute;left:0;top:0;width:1200px;height:610px;}
  .title{
    position:absolute;left:578px;top:58px;margin:0;
    font-size:68px;font-weight:800;font-style:italic;line-height:1;letter-spacing:1px;
    background:linear-gradient(90deg,var(--red),var(--orange) 60%,var(--amber));
    -webkit-background-clip:text;background-clip:text;color:transparent;
  }
  .title-rule{position:absolute;left:640px;top:129px;width:290px;height:3px;background:var(--red);border-radius:2px;}
  .subtitle{position:absolute;margin:0;font-weight:800;font-size:40px;line-height:1;color:var(--ink);}
  .subtitle.line1{left:574px;top:150px;}
  .subtitle.line2{left:624px;top:184px;}
  .edition{
    position:absolute;left:528px;top:261px;width:210px;height:25px;
    background:linear-gradient(90deg,var(--ink) 55%,var(--orange));
    transform:skewX(-25deg);
  }
  .edition span{
    display:block;transform:skewX(25deg);text-align:center;
    color:var(--paper);font-weight:800;font-size:22px;line-height:25px;letter-spacing:.5px;
  }
  .place,.dates,.year{position:absolute;margin:0;font-weight:800;line-height:1;color:var(--ink);text-align:center;width:400px;left:406px;}
  .place{top:292px;font-size:42px;}
  .dates{top:334px;font-size:58px;}
  .year{top:390px;font-size:58px;}
  .program{position:absolute;left:330px;top:472px;width:320px;margin:0;font-weight:700;font-size:24px;line-height:1;}
  .program p{margin:0;}
  .program .day{color:var(--ink);}
  .program .what{color:var(--red);}
  .program .indent{padding-left:90px;}
  .program .second{margin-top:10px;padding-left:25px;}
  .signup{
    position:absolute;left:250px;top:573px;width:320px;height:34px;
    background:var(--brush);transform:skewX(-8deg);
  }
  .signup span{
    display:block;transform:skewX(8deg);text-align:center;
    color:var(--orange);font-weight:700;font-size:18px;line-height:34px;letter-spacing:.5px;
  }
  .logo-slot{
    position:absolute;top:634px;margin:0;
    font-family:"Barlow",Arial,sans-serif;font-style:italic;font-weight:800;font-size:15px;color:#000;
  }
  .logo-slot.small{left:83px;}
  .logo-slot.big{left:965px;}
</style>
</head>
<body>
<main class="poster">
  <svg class="scenery" viewBox="0 0 1200 610" xmlns="http://www.w3.org/2000/svg">
    <defs>
      <linearGradient id="bike-scene" x1="0" y1="0" x2="0.6" y2="1">
        <stop offset="0" stop-color="#9fd6c0"/>
        <stop offset="0.35" stop-color="#f3e7b0"/>
        <stop offset="0.6" stop-color="#4f9f8a"/>
        <stop offset="1" stop-color="#244f3a"/>
      </linearGradient>
      <linearGradient id="run-scene" x1="0" y1="0" x2="0" y2="1">
        <stop offset="0" stop-color="#f7c460"/>
        <stop offset="0.4" stop-color="#f1a94a"/>
        <stop offset="0.62" stop-color="#3fb7b4"/>
        <stop offset="1" stop-color="#1d4a4a"/>
      </linearGradient>
    </defs>
    <polygon points="0,0 610,0 250,610 0,610" fill="url(#bike-scene)" role="img" aria-label="Illustration: mountain bikers riding a dirt trail through green mountains"/>
    <polygon points="920,0 1200,0 1200,610 575,610" fill="url(#run-scene)" role="img" aria-label="Illustration: trail runner on a golden hillside above a river gorge at sunset"/>
  </svg>

  <h1 class="title">DEALUL VULTAN</h1>
  <div class="title-rule"></div>
  <p class="subtitle line1">MOUNTAIN BIKE &amp;</p>
  <p class="subtitle line2">TRAIL RUN RACE</p>

  <div class="edition"><span>EDITIA A-7A</span></div>
  <p class="place">VALEA BRANTULUI</p>
  <p class="dates">8-9 IUNIE</p>
  <p class="year">2024</p>

  <div class="program">
    <p><span class="day">8 IUNIE</span> <span class="what">- Concurs Mountain Bike</span></p>
    <p class="indent what">&amp; Concert</p>
    <p class="second"><span class="day">9 IUNIE</span> <span class="what">- Concurs Trail Run</span></p>
  </div>

  <div class="signup"><span>INSCRIERI PE WWW.BRANTOVELO.RO</span></div>

  <p class="logo-slot small">SMALL LOGOS HERE</p>
  <p class="logo-slot big">BIG LOGOS HERE</p>
</main>
</body>
</html>
```